Electronic call to action mailer

I am launching my new web site and would like to send an electronic mailer to a segmented base. The base would be mostly mothers with children and I want them to shop at my new web site.

I would like to include a call to action - if they register as members they will get 20% off their first purchase and a 10% thereafter as members.

They will also be in a lucky draw contest for a $500 voucher to use at our wen site.
Updates

I have updated the details I require. As this is a call to action page, it should be really catchy that we brand new company that promises to bring quality children's products to them. The company's vision is pinned to producing and distributing organic products and products that are produced with fair trade practices.

Reason: I was late in updating my brief and I think there are a few designs that I already like. I just need to have the updates in

Target Market(s)

Parents that are interested in quality products for kids

Industry/Entity Type

Electronic

Font styles to use
Sans Serif

Colors
c1b2d3
86cfc6
f04a50

Requirements
Must have
• I page that is really easy to get the message. 5 consolation prizes that will be from the Tiny Amber Meadows toiletry range. (picture included). Winner gets $500 worth of goods (at RRP)
Must mention that this is in conjunction with the launch of our new on-line shop.
Must mention that our range of clothes are new to Singapore and we have exclusivity with the brands
terms and conditions apply
Nice to have
• A catchy tag line, making them want to become a member

```html
<!DOCTYPE html>
<html lang="en">
<head>
<meta charset="utf-8">
<title>Wildbloom Kids – Our New Online Shop Is Open</title>
<link rel="stylesheet" href="https://fonts.googleapis.com/css2?family=Montserrat:wght@500;600&family=Questrial&display=swap">
<style>
  :root {
    --page-bg: #dddddd;
    --white: #ffffff;
    --coral: #f04a50;
    --coral-band: #ec4a4f;
    --teal: #86cfc6;
    --teal-bar: #85cec5;
    --lilac: #c1b2d3;
    --ink: #222222;
    --muted: #444444;
    --icon-grey: #7a7a7a;
    --brand-teal: #3d8c8a;
  }
  * { margin: 0; padding: 0; box-sizing: border-box; }
  html, body { width: 879px; height: 1200px; overflow: hidden; }
  body {
    background: var(--page-bg);
    position: relative;
    font-family: "Questrial", "Century Gothic", sans-serif;
    color: var(--ink);
  }
  a { text-decoration: none; }
  .block { position: absolute; }

  /* Header + hero */
  .top-card { left: 96px; top: 0; width: 687px; height: 470px; background: var(--white); }
  .brand { left: 119px; top: 52px; display: flex; align-items: center; gap: 7px; }
  .brand-dot { width: 14px; height: 14px; border-radius: 50%; background: var(--brand-teal); }
  .brand-name { font-family: "Montserrat", sans-serif; font-weight: 600; font-size: 17px; color: var(--brand-teal); line-height: 1; }

  .hero-photo {
    left: 115px; top: 108px; width: 652px; height: 289px;
    background:
      radial-gradient(ellipse 30% 40% at 30% 55%, rgba(70,120,170,.55), transparent 70%),
      radial-gradient(ellipse 25% 45% at 55% 50%, rgba(190,90,80,.45), transparent 70%),
      radial-gradient(ellipse 20% 35% at 72% 45%, rgba(200,130,70,.4), transparent 70%),
      linear-gradient(90deg, #2e3b44 0%, #36434a 55%, #8a7a62 80%, #a69476 100%);
  }
  .hero-band {
    left: 115px; top: 294px; width: 578px; height: 89px;
    background: var(--coral-band); color: var(--white); padding: 5px 0 0 9px;
  }
  .hero-title { font-family: "Montserrat", sans-serif; font-weight: 600; font-size: 33px; line-height: 38px; }
  .hero-sub { font-size: 22.5px; line-height: 22px; }
  .hero-sub strong { font-family: "Montserrat", sans-serif; font-weight: 600; font-size: 21px; }
  .hero-terms { font-size: 9.5px; margin-top: 12px; }

  .more-info { left: 123px; top: 404px; width: 642px; }
  .more-info h2 { font-family: "Montserrat", sans-serif; font-weight: 600; font-size: 20px; color: var(--coral); line-height: 24px; }
  .more-info p { font-size: 12.5px; line-height: 15px; color: var(--ink); }
  .more-info a { color: var(--coral); }

  /* Early bird */
  .early-title { left: 123px; top: 484px; font-family: "Montserrat", sans-serif; font-weight: 600; font-size: 32px; color: var(--coral); line-height: 44px; }
  .early-bird-art { left: 735px; top: 490px; width: 40px; height: 40px; border-radius: 50% 50% 50% 10%; background: var(--coral); }
  .early-band { left: 96px; top: 530px; width: 692px; height: 34px; background: var(--white); padding: 10px 0 0 27px; font-size: 12.4px; color: var(--muted); }
  .early-band strong { font-family: "Montserrat", sans-serif; font-weight: 600; color: var(--ink); }

  .gift-panel { left: 98px; top: 579px; width: 690px; height: 194px; background: var(--teal); }
  .gift-tile { top: 599px; width: 144px; height: 144px; background: var(--white); border-radius: 3px; display: flex; align-items: center; justify-content: center; }
  .gift-art { width: 128px; height: 128px; border-radius: 6px; }
  .gift-puzzle-dragon .gift-art { background: radial-gradient(circle at 50% 50%, #e0903a 0%, #c94a3a 40%, #3fa061 70%, #ffffff 72%); }
  .gift-bus .gift-art { background: linear-gradient(180deg, #ffffff 0%, #e53228 8%, #d8281f 90%, #ffffff 92%); }
  .gift-puzzle-horse .gift-art { background: radial-gradient(circle at 50% 50%, #35b5e0 0%, #d4579a 35%, #5d3b94 62%, #ffffff 66%); }
  .gift-sleepbag .gift-art { width: 90px; background: linear-gradient(180deg, #f6e8e6, #ecd0cd); border-left: 2px solid #d6322c; border-right: 2px solid #d6322c; }

  .member-bar {
    left: 97px; top: 784px; width: 685px; height: 45px; background: var(--teal-bar);
    color: var(--white); font-family: "Montserrat", sans-serif; font-weight: 600; font-size: 23.5px;
    display: flex; align-items: center; padding-left: 27px; gap: 6px;
  }

  /* Register */
  .register-photo {
    left: 99px; top: 843px; width: 684px; height: 153px;
    background:
      radial-gradient(ellipse 22% 60% at 33% 60%, rgba(190,80,80,.55), transparent 70%),
      radial-gradient(ellipse 18% 55% at 52% 65%, rgba(235,130,60,.55), transparent 70%),
      linear-gradient(180deg, #9cc07a 0%, #86b062 55%, #dfe9cd 100%);
  }
  .register-band {
    left: 100px; top: 996px; width: 685px; height: 77px; background: var(--coral-band);
    color: var(--white); padding: 7px 0 0 24px;
  }
  .register-title { font-family: "Montserrat", sans-serif; font-weight: 600; font-size: 31px; line-height: 36px; }
  .register-sub { font-size: 22px; line-height: 24px; }
  .register-arrow { position: absolute; right: 12px; top: 24px; }

  /* Footer */
  .footer { left: 96px; top: 1084px; width: 688px; height: 88px; background: var(--white); }
  .social { top: 1122px; display: flex; align-items: center; gap: 5px; font-size: 12px; color: var(--icon-grey); }
  .social-dot { width: 18px; height: 18px; border-radius: 50%; background: var(--icon-grey); }
</style>
</head>
<body>
  <div class="block top-card"></div>
  <div class="block brand">
    <span class="brand-dot"></span>
    <span class="brand-name">Wildbloom Kids</span>
  </div>

  <div class="block hero-photo" role="img" aria-label="Three young children in colourful printed clothes from our new online shop, playing by a wooden fence"></div>
  <div class="block hero-band">
    <h1 class="hero-title">Win a $500 shopping voucher</h1>
    <p class="hero-sub">get chance to win voucher worth <strong>$500*</strong></p>
    <p class="hero-terms">*terms and conditions apply</p>
  </div>

  <section class="block more-info">
    <h2>More Info</h2>
    <p>Winner gets $500 worth of goods including our range of clothes are new to Singapore and we have exclusivity with the brands. 5 consolation prizes that will be from the Tiny Amber Meadows toiletry range. <a href="#">Enter Here</a></p>
  </section>

  <h2 class="block early-title">Early bird gifts</h2>
  <div class="block early-bird-art" role="img" aria-label="Small illustrated red bird"></div>
  <p class="block early-band">First <strong>5 registrations</strong> will receive premium organic toiletries from Tiny Amber Meadows</p>

  <div class="block gift-panel"></div>
  <div class="block gift-tile gift-puzzle-dragon" style="left:117px"><div class="gift-art" role="img" aria-label="Rainbow wooden dragon alphabet puzzle"></div></div>
  <div class="block gift-tile gift-bus" style="left:285px"><div class="gift-art" role="img" aria-label="Red wooden double-decker toy bus"></div></div>
  <div class="block gift-tile gift-puzzle-horse" style="left:454px"><div class="gift-art" role="img" aria-label="Colourful wooden horse number puzzle"></div></div>
  <div class="block gift-tile gift-sleepbag" style="left:622px"><div class="gift-art" role="img" aria-label="Baby sleeping bag with red dotted print"></div></div>

  <a class="block member-bar" href="#">REGISTER NOW and get 10% member dicount here
    <svg width="20" height="26" viewBox="0 0 20 26" aria-hidden="true"><path d="M4 2 L16 13 L4 24" fill="none" stroke="#ffffff" stroke-width="4"/></svg>
  </a>

  <div class="block register-photo" role="img" aria-label="Mother and daughter lying in a green meadow, celebrating the launch of our new online shop"></div>
  <a class="block register-band" href="#">
    <h2 class="register-title">REGISTER NOW</h2>
    <p class="register-sub">members they will get 20% off their first purchase</p>
    <svg class="register-arrow" width="20" height="30" viewBox="0 0 20 30" aria-hidden="true"><path d="M4 3 L16 15 L4 27" fill="none" stroke="#ffffff" stroke-width="4"/></svg>
  </a>

  <footer class="block footer"></footer>
  <a class="block social" href="#" style="left:556px"><span class="social-dot"></span>Kinbook</a>
  <a class="block social" href="#" style="left:636px"><span class="social-dot"></span>Chirper</a>
  <a class="block social" href="#" style="left:714px"><span class="social-dot"></span>Loop</a>
</body>
</html>
```